'Gravelmoth Co' Business Cards

Gravelmoth Co is a clothing company geared toward people in the mining industry who are crushing it (literally) We need a design for a business card that has 'GM' similar to the layout of the inspo photo below. Rock textures and maybe some rock dust (see GIF). I Included SVG of our circle logo but not sure how to include without it being boring, would like some ideas. Front should say 'Gravelmoth Co.' (and 'clothing' in smaller letters below) Back should have our webpage 'gravelmothco.ca' our email 'info@gravelmothco.ca' plus a FB and IG icon

```html
<!DOCTYPE html>
<html lang="en">
<head>
<meta charset="utf-8">
<title>Gravelmoth Co – Business Cards</title>
<link rel="stylesheet" href="https://fonts.googleapis.com/css2?family=Archivo+Black&family=Montserrat:wght@500;700&display=swap">
<style>
  :root {
    --backdrop: #8b8b8c;
    --card: #1e1e1f;
    --card-edge: #141414;
    --chrome: #b9babc;
    --chrome-dim: #6d6e70;
    --gloss: #4a4a4c;
    --band: #3d3829;
    --band-text: #f2f2f2;
    --rock-light: #6e6a62;
    --rock-dark: #2e2b26;
    --icon: #d9d9d9;
  }
  * { box-sizing: border-box; margin: 0; padding: 0; }
  html, body {
    width: 1200px;
    height: 1157px;
    overflow: hidden;
    background: var(--backdrop);
  }
  .sheet {
    position: relative;
    width: 1200px;
    height: 1157px;
  }
  .card {
    position: absolute;
    width: 700px;
    height: 400px;
    background: var(--card);
    border-bottom: 6px solid var(--band);
    box-shadow: 0 6px 0 var(--card-edge);
    overflow: hidden;
  }

  /* Front */
  .card--front { left: 130px; top: 150px; }
  .card--front .rock-disc {
    position: absolute;
    left: 30px;
    top: 40px;
    width: 320px;
    height: 320px;
  }
  .card--front .wordmark {
    position: absolute;
    left: 380px;
    top: 168px;
    width: 300px;
    text-align: center;
  }
  .wordmark__name {
    font-family: "Archivo Black", sans-serif;
    font-size: 31px;
    letter-spacing: 0.5px;
    color: var(--chrome);
    line-height: 1;
  }
  .wordmark__sub {
    margin-top: 8px;
    font-family: "Montserrat", sans-serif;
    font-weight: 500;
    font-size: 12px;
    letter-spacing: 7px;
    color: var(--chrome-dim);
    text-transform: uppercase;
  }

  /* Back */
  .card--back { left: 370px; top: 620px; }
  .card--back .social {
    position: absolute;
    right: 34px;
    top: 28px;
    display: flex;
    gap: 8px;
  }
  .card--back .brand {
    position: absolute;
    left: 60px;
    top: 150px;
    display: flex;
    align-items: center;
    gap: 16px;
  }
  .brand__name {
    font-family: "Archivo Black", sans-serif;
    font-size: 50px;
    color: var(--gloss);
    line-height: 1;
  }
  .card--back .contact-band {
    position: absolute;
    left: 0;
    right: 0;
    bottom: 40px;
    height: 40px;
    background: var(--band);
    display: flex;
    align-items: center;
    justify-content: center;
    font-family: "Montserrat", sans-serif;
    font-weight: 700;
    font-size: 16px;
    letter-spacing: 0.5px;
    color: var(--band-text);
    text-transform: uppercase;
  }
  .contact-band__divider { margin: 0 8px; }
</style>
</head>
<body>
<main class="sheet">

  <section class="card card--front" aria-label="Card front">
    <svg class="rock-disc" viewBox="0 0 320 320" role="img" aria-label="Rock texture disc">
      <defs>
        <radialGradient id="rockGrad" cx="35%" cy="35%" r="75%">
          <stop offset="0%" stop-color="var(--rock-light)"/>
          <stop offset="100%" stop-color="var(--rock-dark)"/>
        </radialGradient>
      </defs>
      <circle cx="160" cy="160" r="158" fill="url(#rockGrad)"/>
    </svg>
    <div class="wordmark">
      <div class="wordmark__name">GRAVELMOTH CO.</div>
      <div class="wordmark__sub">Clothing</div>
    </div>
  </section>

  <section class="card card--back" aria-label="Card back">
    <div class="social" aria-label="Social media">
      <svg width="26" height="26" viewBox="0 0 26 26" aria-hidden="true"><circle cx="13" cy="13" r="12" fill="var(--icon)"/></svg>
      <svg width="26" height="26" viewBox="0 0 26 26" aria-hidden="true"><circle cx="13" cy="13" r="12" fill="var(--icon)"/></svg>
    </div>
    <div class="brand">
      <svg width="52" height="52" viewBox="0 0 52 52" aria-hidden="true"><circle cx="26" cy="26" r="25" fill="var(--gloss)"/></svg>
      <span class="brand__name">GRAVELMOTH CO.</span>
    </div>
    <div class="contact-band">
      <span>info@gravelmothco.ca</span>
      <span class="contact-band__divider">|</span>
      <span>www.gravelmothco.ca</span>
    </div>
  </section>

</main>
</body>
</html>
```